a business advisory consulting website

I need a website 3-5 pages to sell my professional services in IT and Project management Consulting. My company name is Northwell Strategy Consulting. I want it to be device friendly and easy to navigate for the busy executive however intriguing enough.
I have attached some info I drafted on About the company and personal Bio. Also there is a website that I really like that I have attached the initial site pdf and websites that I like are here: https://quillmarshcapital.example, https://tandermoviews.example, https://www.felkinlearningconsulting.example as examples. Thanks
Updates

Hi Designers, I have uploaded the logo in 3D .png format, to assist in the web design.

Target Market(s)

B2B, governments, IT companies, Project Management companies and Consulting firms, small medium enterprises to large corporate enterprises.

Industry/Entity Type

It Professional

Coding

Coded - Design and coding required

Number of Pages Required

5+ page

Font styles to use
Sans Serif

Requirements
Must have
• Home, About company, the team, what we do and contact us
Nice to have
• Blog
Should not have
• pop ups, flash

```html
<!DOCTYPE html>
<html lang="en">
<head>
<meta charset="utf-8">
<title>Northwell Strategy Consulting</title>
<link rel="stylesheet" href="https://fonts.googleapis.com/css2?family=Nunito+Sans:wght@300;400;700;800&family=Open+Sans:wght@400;600&display=swap">
<style>
:root{
  --navy:#1f2544;
  --navy-deep:#1b2040;
  --navy-band:#262c50;
  --red:#e3222b;
  --ink:#2a2f4a;
  --text:#4a4e60;
  --grey-band:#f4f4f5;
  --bio-bg:#f7f7f8;
  --white:#ffffff;
  --field:#2a3052;
  --field-line:#4a5070;
}
*{box-sizing:border-box;margin:0;padding:0}
html,body{width:1200px;height:2373px;overflow:hidden}
body{position:relative;background:var(--white);font-family:"Open Sans",sans-serif;color:var(--text);font-size:9.6px;line-height:15px}
.abs{position:absolute}
p{margin-bottom:12px}
.heading{font-family:"Nunito Sans",sans-serif;font-weight:300;color:var(--ink);font-size:33px;line-height:39px}

/* header */
.brand{left:242px;top:22px;display:flex;align-items:center;gap:7px;font-family:"Nunito Sans",sans-serif;font-weight:800;font-size:14px;color:var(--navy)}
.brand-mark{width:14px;height:14px;background:var(--red)}
.nav{left:645px;top:30px;display:flex;gap:25px;font-size:8.4px;color:var(--ink);letter-spacing:.1px}

/* hero */
.world-map{left:134px;top:69px;width:942px;height:415px;background:radial-gradient(ellipse at 55% 45%,#e9eaee 0%,#f4f4f6 55%,rgba(255,255,255,0) 75%)}
.hero-title{left:244px;top:140px;font-family:"Nunito Sans",sans-serif;font-weight:800;font-size:40px;line-height:50px;color:var(--navy)}
.hero-title small{font-size:14px;color:var(--red);font-weight:700;margin-left:8px}
.hero-lead{left:244px;top:212px;width:670px;font-family:"Nunito Sans",sans-serif;font-weight:700;font-size:20px;line-height:26px;color:var(--navy)}
.btn-start{left:244px;top:290px;width:84px;height:23px;background:var(--red);color:var(--white);font-size:8.4px;line-height:23px;text-align:center}
.hero-contact{top:357px;display:flex;align-items:center;gap:9px;font-size:9.4px;color:var(--ink)}

/* sections */
.band-grey{left:0;top:700px;width:1200px;height:322px;background:var(--grey-band)}
.band-navy{left:0;top:1212px;width:1200px;height:264px;background:var(--navy)}
.band-bio{left:0;top:1476px;width:1200px;height:528px;background:var(--bio-bg)}
.on-navy{color:#d7d9e3}
.on-navy.heading{color:#e9eaf0}

.portrait{left:114px;top:1600px;width:202px;height:202px;border-radius:50%;background:radial-gradient(circle at 50% 40%,#d9cfc6 0%,#b8aca2 45%,#3a3f52 100%)}
.bio-name{left:119px;top:1843px;font-family:"Nunito Sans",sans-serif;font-weight:800;font-size:20px;color:var(--navy)}

/* footer */
.footer{left:0;top:2004px;width:1200px;height:338px;background:var(--navy-deep)}
.footer-base{left:0;top:2342px;width:1200px;height:31px;background:var(--navy-band)}
.footer-brand{left:238px;top:2070px;display:flex;align-items:center;gap:8px;font-family:"Nunito Sans",sans-serif;font-weight:800;font-size:22px;color:var(--white)}
.footer-brand .brand-mark{width:20px;height:20px}
.footer-line{left:226px;display:flex;align-items:center;gap:8px;font-size:9.4px;color:#e4e6ee}
.field{left:622px;width:353px;height:24px;border:1px solid var(--field-line);background:var(--field);color:#9ea3b8;font-size:9px;line-height:22px;padding-left:7px}
.field.area{height:37px;line-height:14px;padding-top:4px}
.check{left:622px;top:2255px;display:flex;align-items:center;gap:14px;font-size:9px;font-weight:600;color:#e4e6ee}
.check span{width:10px;height:10px;border:1px solid var(--field-line);background:var(--field)}
.btn-send{left:622px;top:2275px;width:353px;height:22px;background:var(--red);color:var(--white);font-size:8.4px;line-height:22px;text-align:center}
.copyright{left:226px;top:2352px;font-size:8px;color:#c8cbd8}
.icon{width:11px;height:11px;flex:none}
</style>
</head>
<body>

<header>
  <div class="abs brand"><span class="brand-mark"></span>Northwell Strategy Consulting</div>
  <nav class="abs nav"><span>WHAT WE CAN DO</span><span>BLOG</span><span>ABOUT US</span><span>OUR TEAM</span><span>CONTACT US</span></nav>
</header>

<section class="hero">
  <div class="abs world-map" role="img" aria-label="Dotted world map in light grey"></div>
  <h1 class="abs hero-title">Northwell Strategy Consulting<small>Pty, Ltd.</small></h1>
  <p class="abs hero-lead">To get started straight away, simply tap any placeholder text (such as this) and start typing.</p>
  <div class="abs btn-start">START NOW</div>
  <div class="abs hero-contact" style="left:573px">
    <svg class="icon" viewBox="0 0 12 12" fill="none" stroke="#555a70" stroke-width="0.9"><path d="M2.5 1.2l2 2-1.1 1.3a7 7 0 0 0 4.1 4.1l1.3-1.1 2 2-1.3 1.3C5.4 10.8 1.2 6.6 1.2 2.5z"/></svg>
    <span>+254 700 418 220 / +254 711 562 304</span>
  </div>
  <div class="abs hero-contact" style="left:782px">
    <svg class="icon" viewBox="0 0 12 12" fill="none" stroke="#555a70" stroke-width="0.9"><rect x="1" y="2.5" width="10" height="7"/><path d="M1 2.5l5 4 5-4"/></svg>
    <span>hello@quillmarshcapital.example</span>
  </div>
</section>

<section class="why">
  <h2 class="abs heading" style="left:226px;top:561px;width:220px">Why We Exists ?</h2>
  <div class="abs" style="left:490px;top:541px;width:470px">
    <p>Our aim at Quillmarsh Capital is to be a leading strategy and financial advisory firm across the continent solving complex management problems for small and medium sized enterprises across a wide range of industries.</p>
    <p>We help you scale your business operations to become highly profitable.</p>
    <p>We offer your organization cutting-edge expertise leveraging on first-class, strategic and financial insights that help you simplify and structure your processes to become a lean efficient enterprise.</p>
  </div>
</section>

<section class="government">
  <div class="abs band-grey"></div>
  <div class="abs" style="left:226px;top:744px;width:480px">
    <p>Across the three levels of Government – Federal, State/Territory and Local – leaders continually face complex decisions around how to allocate limited resources to best service their citizens. In the past, Governments have faced criticism for an over reliance on bureaucracy and an inability to adapt or even prepare for the future. However, the trend among global leaders now is one of innovation both in how they run the business of Government and in the services they apply their resources to. Programs of innovation and transformation are actively sponsored to promote a more competitive and viable society. A focus on reducing waste is leading to more efficient, cost effective government bodies underpinned by the adoption of technology and process improvement techniques. And of course the safety and security (physical and data) of its citizens remains a primary goal in a world facing an unparalleled level of technological advance.</p>
    <p>We work closely with public sector bodies to drive cost and efficiency gains through best practise process excellence programs and identify &amp; implement opportunities to improve the</p>
    <p>customer experience. We understand the traditional challenges of the public sector and that each level of Government faces its own unique challenges. To this we bring deep expertise in process excellence and a pragmatic approach to the application of these techniques to drive improvement.</p>
  </div>
  <h2 class="abs heading" style="left:755px;top:785px;width:260px">Process Improvement Within Government ?</h2>
</section>

<section class="about">
  <h2 class="abs heading" style="left:226px;top:1099px">About Us ?</h2>
  <div class="abs" style="left:490px;top:1067px;width:480px">
    <p>We are a specialist operational excellence firm, delivering consulting and advisory services in six core capabilities, across all industries and all business lines to improve performance, efficiency, profitability, automation and scalability, for clients across Australia.</p>
    <p>We’re known for our pragmatism, in depth analysis, strategic insight and nurturing long-term client self-sufficiency. We approach business consulting differently, with a Genuine Client Partnership model that builds client capability and rightsized solutions for the client.</p>
  </div>
</section>

<section class="healthcare">
  <div class="abs band-navy"></div>
  <div class="abs on-navy" style="left:226px;top:1256px;width:490px">
    <p>Australia’s health care system is a complex web of public and private providers, settings, participants and supporting mechanisms. Health providers include medical practitioners, nurses, allied and other health professionals, hospitals, clinics and government agencies and private providers. These providers deliver a complete range of services across many levels, from public health and preventive services in the community, to primary health care, emergency health services, hospital-based treatment, and rehabilitation and palliative care.</p>
    <p>We work closely with both the Public sector health services through the 3 levels of government and the Private sector health service providers to drive efficiency across their diverse range of services. Through best practise business process re-engineering, the pragmatic use of toolsets such as Lean Flow Method and a deep understanding of Business &amp; Technology Change, we drive significant cost and efficiency gains across all types of healthcare from hospital to aged care facilities and everything in between.</p>
  </div>
  <h2 class="abs heading on-navy" style="left:755px;top:1288px;width:260px">Technology Analysis Within Healthcare ?</h2>
</section>

<section class="bio">
  <div class="abs band-bio"></div>
  <div class="abs portrait" role="img" aria-label="Portrait photo of the consultant"></div>
  <h3 class="abs bio-name">Daniel Karimi Bio</h3>
  <div class="abs" style="left:429px;top:1522px;width:348px">
    <p>Daniel Karimi is an IT professional with more than 20 years of experience turning business initiatives into technology solutions. His expertise has been identifying deficiencies and developing or facilitating the best solutions for an outcome that is satisfactory to all stakeholders involved.</p>
    <p>Daniel improves business processes as older organizations restructure or migrate to newer technologies. He bridges the gap between the actual people in these organizations transitioning and the new technologies they seek which is a value add to any organization’s success.</p>
    <p>His clients benefit from his years of experience in technology projects ranging from infrastructure at Australian blue-chip listed companies, healthcare, non-profit, education, and state government agencies and departments to state a few.</p>
    <p>He specializes in business process improvement and strategy development utilizing best practice frameworks to deliver quality outcomes. He promotes organizational growth and optimizing business processes by taking complex organizational problems and mapping out bite-sized solutions that exploit technology usage thus simplifying the end user’s day to day job as well as capturing data for future benchmarks.</p>
  </div>
  <div class="abs" style="left:806px;top:1522px;width:352px">
    <p>Most of his work is contract-based – nine to 18 months on average – making his project deliverables and timeframe concise. He consults on transformation projects which are usually short term, goal-oriented, and meant to technologically advance an organization forward through their business processes. Once he delivers the process for the new technology or restructure, his work is done.</p>
    <p>Daniel’s experience has seen him reducing operational workforce costs by 5% through a review of workforce management processes and optimizing human performance at one organization, as well as transitioning over 100,000 staff members from a perpetual Deskline Office license model to a Deskline Cloud user-based subscription model at another organization.</p>
    <p>He has also been a strategic advisor consulting with business teams to ensure the alignment of project objectives with government IT strategy as well as being instrumental in facilitating and developing a cloud strategy for another organization – obtaining and setting up cloud brokerage services with Nimbusreach Cloud and Stratovane Cloud services.</p>
    <p>His stakeholder management skills have enabled him to build strong, long-lasting, and collaborative relationships with a broad range of senior internal and external stakeholders, while also taking a lead role in the development of effective stakeholder relationship strategies.</p>
    <p>Daniel applies various business analysis techniques to gather requirements directly from stakeholders, inspects existing systems and documentation, and identifies and references department and whole-of-government policies and standards. He uses structured interviews, process mapping, storyboarding, forcefield analysis, communication plans, and stakeholder engagement plans to effectively implement project changes.</p>
  </div>
</section>

<footer>
  <div class="abs footer"></div>
  <div class="abs footer-brand"><span class="brand-mark"></span>Northwell Strategy Consulting</div>
  <div class="abs footer-line" style="top:2147px">
    <svg class="icon" viewBox="0 0 12 12" fill="none" stroke="#c8cbd8" stroke-width="0.9"><path d="M2.5 1.2l2 2-1.1 1.3a7 7 0 0 0 4.1 4.1l1.3-1.1 2 2-1.3 1.3C5.4 10.8 1.2 6.6 1.2 2.5z"/></svg>
    <span>+254 700 418 220 / +254 711 562 304</span>
  </div>
  <div class="abs footer-line" style="top:2187px">
    <svg class="icon" viewBox="0 0 12 12" fill="none" stroke="#c8cbd8" stroke-width="0.9"><rect x="1" y="2.5" width="10" height="7"/><path d="M1 2.5l5 4 5-4"/></svg>
    <span>hello@quillmarshcapital.example</span>
  </div>
  <div class="abs footer-line" style="top:2227px">
    <svg class="icon" viewBox="0 0 12 12" fill="none" stroke="#c8cbd8" stroke-width="0.9"><path d="M6 11s-3.6-4-3.6-6.4a3.6 3.6 0 0 1 7.2 0C9.6 7 6 11 6 11z"/><circle cx="6" cy="4.6" r="1.3"/></svg>
    <span>9th Floor, Wing C, Harbourline House, Cedar Lane</span>
  </div>
  <div class="abs footer-line" style="top:2266px">
    <svg class="icon" viewBox="0 0 12 12" fill="none" stroke="#c8cbd8" stroke-width="0.9"><path d="M6 11s-3.6-4-3.6-6.4a3.6 3.6 0 0 1 7.2 0C9.6 7 6 11 6 11z"/><circle cx="6" cy="4.6" r="1.3"/></svg>
    <span>P.O. Box 40210 – 00100, Nairobi</span>
  </div>

  <div class="abs field" style="top:2049px">yourname</div>
  <div class="abs field" style="top:2086px">organization</div>
  <div class="abs field" style="top:2124px">phone</div>
  <div class="abs field" style="top:2161px">email</div>
  <div class="abs field area" style="top:2197px">write us a messages</div>
  <div class="abs check"><span></span>Request brochure/company profile.</div>
  <div class="abs btn-send">SEND</div>

  <div class="abs footer-base"></div>
  <div class="abs copyright">Copyright 2020, Northwell Strategy Consulting. All Right Reserved.</div>
</footer>

</body>
</html>
```